Nine Rung Ledger Remedy Seminar

I would like a flyer to hand out to participants at the speeches that we give. We are a CPA firm that specializes in entrepreneurs and realtors. We would like a flyer that looks crisp and clean, that integrates our logo and our company colors (shades of blue & gold). We would like the wording to be as laid out in the attached documents, but design is up to you. We would like a picture to go along with each point and are open to ideas. The flyer should be one page, preferably just the front.

Colors
3176b5
fee18a

Requirements
Must have
• Our logo and the wording supplied.
• A picture to go along with each topic.
Nice to have
• Images that pop, clean look, professional.
Should not have
• Look messy.

```html
<!DOCTYPE html>
<html lang="en">
<head>
<meta charset="utf-8">
<title>Nine Rung Ledger Remedy Seminar Agenda</title>
<link rel="stylesheet" href="https://fonts.googleapis.com/css2?family=Oswald:wght@600;700&family=Open+Sans:ital,wght@0,400;0,700;0,800;1,400&family=Arimo:wght@400&family=Libre+Baskerville:ital,wght@1,700&display=swap">
<style>
:root{
  --backdrop:#2a2a2a;
  --paper:#ffffff;
  --brand-blue:#3176b5;
  --navy:#1f4f8a;
  --gold:#fee18a;
  --gold-deep:#f5c024;
  --slate:#3f7391;
  --teal:#3aa6a0;
  --royal:#2e5b9e;
  --red:#d9344f;
  --panel:#f5f6f9;
  --ink:#2e2e2e;
  --fold:#555555;
}
*{margin:0;padding:0;box-sizing:border-box}
html,body{width:900px;height:1200px;overflow:hidden;background:var(--backdrop)}
.canvas{position:relative;width:900px;height:1200px}
.flyer{position:absolute;left:75px;top:110px;width:737px;height:952px;background:var(--paper);overflow:hidden}
.tab{position:absolute;top:0;width:40px;height:42px;background:var(--gold)}
.tab--left{left:0}.tab--right{right:0}
.fold{position:absolute;top:64px;width:0;height:0;border-top:20px solid var(--fold)}
.fold--left{left:18px;border-left:20px solid transparent}
.fold--right{right:18px;border-right:20px solid transparent}
.header{position:absolute;left:38px;top:0;width:661px;height:95px;background:var(--brand-blue);display:flex;align-items:center;justify-content:center}
.header h1{font-family:"Oswald",sans-serif;font-weight:700;font-size:31px;color:#fff;letter-spacing:.2px}
.step{position:absolute;left:0;width:737px;height:88px}
.step__label{position:absolute;left:0;top:32px;width:37px;height:17px;background:var(--brand-blue);color:#fff;font-family:"Oswald",sans-serif;font-weight:600;font-size:12px;line-height:17px;text-align:center}
.step__num{position:absolute;left:44px;top:17px;font-family:"Open Sans",sans-serif;font-size:31px;color:var(--brand-blue);line-height:1}
.step__panel{position:absolute;left:115px;top:0;width:531px;height:100%;background:var(--panel)}
.step__bar{position:absolute;left:647px;top:0;width:18px;height:100%}
.step__icon{position:absolute;left:66px;top:-2px;width:92px;height:92px}
.step__text{position:absolute;left:159px;top:50%;transform:translateY(-50%);width:452px;font-family:"Open Sans",sans-serif;font-size:13.3px;line-height:18px;color:var(--ink);text-align:justify}
.swoosh{position:absolute;left:0;top:735px;width:737px;height:80px}
.brand{position:absolute;left:0;top:768px;width:737px;text-align:center}
.brand__name{font-family:"Open Sans",sans-serif;font-weight:800;font-size:30px;color:var(--navy);letter-spacing:.5px}
.brand__tag{font-family:"Libre Baskerville",serif;font-style:italic;font-weight:700;font-size:9px;color:#222;margin-top:2px}
.ribbon{position:absolute;left:98px;top:840px;width:546px;height:32px}
.ribbon__text{position:absolute;left:0;top:0;width:100%;height:100%;display:flex;align-items:center;justify-content:center;font-family:"Oswald",sans-serif;font-weight:600;font-size:17px;color:var(--brand-blue)}
.contacts{position:absolute;left:48px;top:880px;width:650px;height:70px;font-family:"Arimo",sans-serif;font-size:14px;color:#222}
.contacts__col{position:absolute;top:0}
.contacts__row{display:flex;align-items:flex-start;gap:8px;line-height:17px;margin-bottom:6px}
.contacts__divider{position:absolute;top:0;width:1px;height:52px;background:var(--brand-blue)}
.contacts__icon{width:18px;height:18px;flex:none}
</style>
</head>
<body>
<div class="canvas">
<div class="flyer">
  <div class="tab tab--left"></div><div class="tab tab--right"></div>
  <div class="fold fold--left"></div><div class="fold fold--right"></div>
  <header class="header"><h1>NINE RUNG LEDGER REMEDY SEMINAR AGENDA</h1></header>

  <!-- Step 1 -->
  <section class="step" style="top:110px">
    <div class="step__label">STEP</div><div class="step__num">1</div>
    <div class="step__panel"></div><div class="step__bar" style="background:var(--slate)"></div>
    <svg class="step__icon" viewBox="0 0 92 92"><path d="M46 4a42 42 0 0 0 0 84" fill="none" stroke="var(--slate)" stroke-width="6"/><circle cx="46" cy="46" r="33" fill="var(--slate)"/>
      <path d="M34 28h18l7 7v28H34z" fill="none" stroke="#fff" stroke-width="2.5"/><path d="M39 38h12M39 44h12M39 50h6" stroke="#fff" stroke-width="2"/><circle cx="53" cy="56" r="7" fill="#fff"/><path d="M50 59l6-6" stroke="var(--slate)" stroke-width="1.5"/></svg>
    <p class="step__text">We will first show you how to eliminate much of your self-employment tax on your return by converting your business into an S Corporation. A business owner making over $120,000 per year can save about $12,000 per year by doing this.</p>
  </section>

  <!-- Step 2 -->
  <section class="step" style="top:205px;height:86px">
    <div class="step__label">STEP</div><div class="step__num">2</div>
    <div class="step__panel"></div><div class="step__bar" style="background:var(--gold-deep)"></div>
    <svg class="step__icon" viewBox="0 0 92 92"><path d="M46 4a42 42 0 0 0 0 84" fill="none" stroke="var(--gold-deep)" stroke-width="6"/><circle cx="46" cy="46" r="33" fill="var(--gold-deep)"/>
      <circle cx="50" cy="36" r="9" fill="none" stroke="#fff" stroke-width="2.5"/><text x="50" y="40" font-family="Open Sans,sans-serif" font-size="11" font-weight="700" fill="#fff" text-anchor="middle">$</text><path d="M30 52h6v14h-6zM36 55h10l12-3c3 0 3 4 0 5l-10 4H36" fill="#fff"/></svg>
    <p class="step__text">We will show you how to get tax free income from your corporation by renting you home to the corporation for the board meetings. Many of our clients are getting up to $21,000 in tax free income which could put $8,400 cash into your pocket.</p>
  </section>

  <!-- Step 3 -->
  <section class="step" style="top:295px;height:86px">
    <div class="step__label">STEP</div><div class="step__num">3</div>
    <div class="step__panel"></div><div class="step__bar" style="background:var(--teal)"></div>
    <svg class="step__icon" viewBox="0 0 92 92"><path d="M46 4a42 42 0 0 0 0 84" fill="none" stroke="var(--teal)" stroke-width="6"/><circle cx="46" cy="46" r="33" fill="var(--teal)"/>
      <circle cx="50" cy="36" r="9" fill="none" stroke="#fff" stroke-width="2.5"/><text x="50" y="40" font-family="Open Sans,sans-serif" font-size="11" font-weight="700" fill="#fff" text-anchor="middle">$</text><path d="M30 52h6v14h-6zM36 55h10l12-3c3 0 3 4 0 5l-10 4H36" fill="#fff"/></svg>
    <p class="step__text">We will show you the easiest way to track your expenses so that the only thing you will have to do to have rock solid books is to take a picture of the receipt and throw it away. &nbsp; It doesn’t get any better than that.</p>
  </section>

  <!-- Step 4 -->
  <section class="step" style="top:385px;height:85px">
    <div class="step__label">STEP</div><div class="step__num">4</div>
    <div class="step__panel"></div><div class="step__bar" style="background:var(--royal)"></div>
    <svg class="step__icon" viewBox="0 0 92 92"><path d="M46 4a42 42 0 0 0 0 84" fill="none" stroke="var(--royal)" stroke-width="6"/><circle cx="46" cy="46" r="33" fill="var(--royal)"/>
      <rect x="44" y="28" width="22" height="16" fill="none" stroke="#fff" stroke-width="2"/><path d="M47 40l5-5 4 3 6-6" stroke="#fff" stroke-width="1.5" fill="none"/><circle cx="34" cy="33" r="4" fill="#fff"/><path d="M29 50v-9h10l5 3" stroke="#fff" stroke-width="3" fill="none"/><circle cx="32" cy="58" r="3" fill="#fff"/><circle cx="46" cy="58" r="3" fill="#fff"/><circle cx="60" cy="58" r="3" fill="#fff"/><path d="M27 66h10M41 66h10M55 66h10" stroke="#fff" stroke-width="4"/></svg>
    <p class="step__text">Next, we show you the importance of tax planning and why it is critical to meet with your CPA before the end of the year and not just when you do your tax preparation.</p>
  </section>

  <!-- Step 5 -->
  <section class="step" style="top:473px;height:82px">
    <div class="step__label">STEP</div><div class="step__num">5</div>
    <div class="step__panel"></div><div class="step__bar" style="background:var(--red)"></div>
    <svg class="step__icon" viewBox="0 0 92 92"><path d="M46 4a42 42 0 0 0 0 84" fill="none" stroke="var(--red)" stroke-width="6"/><circle cx="46" cy="46" r="33" fill="var(--red)"/>
      <circle cx="37" cy="34" r="6" fill="#fff"/><path d="M31 42h12v12h-3v10h-2v-10h-2v10h-2v-10h-3z" fill="#fff"/><circle cx="56" cy="34" r="6" fill="#fff"/><path d="M52 42h8l4 14h-5v8h-2v-8h-2v8h-2v-8h-5z" fill="#fff"/></svg>
    <p class="step__text">We will show you how to hire your children and get $7,500 per child tax free. This will save you $3,000 per child in income tax reduction.</p>
  </section>

  <!-- Step 6 -->
  <section class="step" style="top:562px;height:84px">
    <div class="step__label">STEP</div><div class="step__num">6</div>
    <div class="step__panel"></div><div class="step__bar" style="background:var(--teal)"></div>
    <svg class="step__icon" viewBox="0 0 92 92"><path d="M46 4a42 42 0 0 0 0 84" fill="none" stroke="var(--teal)" stroke-width="6"/><circle cx="46" cy="46" r="33" fill="var(--teal)"/>
      <rect x="28" y="52" width="36" height="9" rx="2" fill="none" stroke="#fff" stroke-width="2.5"/><rect x="31" y="42" width="32" height="9" rx="2" fill="none" stroke="#fff" stroke-width="2.5"/><rect x="29" y="32" width="34" height="9" rx="2" fill="none" stroke="#fff" stroke-width="2.5"/></svg>
    <p class="step__text">We will discuss how to make your child’s college education tax deductible. With college cost spiraling out of control this is a biggie. Most of our clients have a savings of about $12,000 per year of college.</p>
  </section>

  <!-- Step 7 -->
  <section class="step" style="top:650px;height:86px">
    <div class="step__label">STEP</div><div class="step__num">7</div>
    <div class="step__panel"></div><div class="step__bar" style="background:var(--gold-deep)"></div>
    <svg class="step__icon" viewBox="0 0 92 92"><path d="M46 4a42 42 0 0 0 0 84" fill="none" stroke="var(--gold-deep)" stroke-width="6"/><circle cx="46" cy="46" r="33" fill="var(--gold-deep)"/>
      <path d="M40 26h12l-3 7c10 4 14 14 12 22-2 7-8 9-15 9s-13-2-15-9c-2-8 2-18 12-22z" fill="#fff"/><text x="46" y="57" font-family="Open Sans,sans-serif" font-size="16" font-weight="700" fill="var(--gold-deep)" text-anchor="middle">$</text></svg>
    <p class="step__text">Our grand finale is to show you how to use, not one, but two corporations to get a several hundred thousand dollar tax deferral, get an interest free loan from the government and use that money to grow your business and your wealth.</p>
  </section>

  <svg class="swoosh" viewBox="0 0 737 80" preserveAspectRatio="none">
    <path d="M0 48Q368 -10 737 40V22Q368 -28 0 34Z" fill="var(--brand-blue)"/>
    <path d="M0 56Q368 4 737 48" fill="none" stroke="var(--gold-deep)" stroke-width="2"/>
  </svg>

  <div class="brand">
    <div class="brand__name">LEDGERLINE PARTNERS</div>
    <div class="brand__tag">A Professional Accounting Corporation</div>
  </div>

  <div class="ribbon">
    <svg width="546" height="32" viewBox="0 0 546 32"><path d="M0 2h546l-12 14 12 14H0l12-14z" fill="var(--gold)"/></svg>
    <div class="ribbon__text">If they drive by with a machine gun you don’t have to stand up.</div>
  </div>

  <div class="contacts">
    <div class="contacts__col" style="left:0">
      <div class="contacts__row"><svg class="contacts__icon" viewBox="0 0 18 18"><path d="M9 1a6 6 0 0 1 6 6c0 5-6 10-6 10S3 12 3 7a6 6 0 0 1 6-6z" fill="none" stroke="var(--brand-blue)" stroke-width="2"/><circle cx="9" cy="7" r="2" fill="var(--brand-blue)"/></svg><span>2871 Orchard Ave, Ste. B,<br>Calverton, CA 95012</span></div>
    </div>
    <div class="contacts__divider" style="left:202px"></div>
    <div class="contacts__col" style="left:220px">
      <div class="contacts__row"><svg class="contacts__icon" viewBox="0 0 18 18"><circle cx="9" cy="9" r="8" fill="none" stroke="var(--brand-blue)" stroke-width="1.5"/><path d="M6 5l2 2-1 1.5c.7 1.4 1.6 2.3 3 3L11.5 10l2 2-1.5 1.5C8.5 13 5 9.5 4.5 6z" fill="var(--brand-blue)"/></svg><span>555-014-2271</span></div>
      <div class="contacts__row"><svg class="contacts__icon" viewBox="0 0 18 18"><circle cx="9" cy="9" r="8" fill="none" stroke="var(--brand-blue)" stroke-width="1.5"/><rect x="5" y="7" width="8" height="6" fill="var(--brand-blue)"/><rect x="6.5" y="4" width="5" height="3" fill="none" stroke="var(--brand-blue)"/></svg><span>555-014-2290</span></div>
    </div>
    <div class="contacts__divider" style="left:368px"></div>
    <div class="contacts__col" style="left:394px">
      <div class="contacts__row"><svg class="contacts__icon" viewBox="0 0 18 18"><circle cx="9" cy="9" r="8" fill="none" stroke="var(--brand-blue)" stroke-width="1.5"/><rect x="4.5" y="6" width="9" height="6" fill="var(--brand-blue)"/><path d="M4.5 6l4.5 3.5L13.5 6" stroke="#fff" fill="none"/></svg><span>Dana@ledgerlinecpas.com</span></div>
      <div class="contacts__row"><svg class="contacts__icon" viewBox="0 0 18 18"><circle cx="9" cy="9" r="8" fill="none" stroke="var(--brand-blue)" stroke-width="1.5"/><rect x="4.5" y="6" width="9" height="6" fill="var(--brand-blue)"/><path d="M4.5 6l4.5 3.5L13.5 6" stroke="#fff" fill="none"/></svg><span>Morgan@ledgerlinecpas.com</span></div>
      <div class="contacts__row"><svg class="contacts__icon" viewBox="0 0 18 18"><circle cx="9" cy="9" r="8" fill="none" stroke="var(--brand-blue)" stroke-width="1.5"/><circle cx="9" cy="9" r="5" fill="none" stroke="var(--brand-blue)"/><path d="M4 9h10M9 4c-2 3-2 7 0 10M9 4c2 3 2 7 0 10" stroke="var(--brand-blue)" fill="none"/></svg><span>www.ledgerlinecpa.com</span></div>
    </div>
  </div>
</div>
</div>
</body>
</html>
```